Need a solid log.
My company Sales: OrbiqView, Plate Linkway, Valtor Internet
Design and installation of WI_FI systems.
Fulfillment company for installations in the Electronics industry

Industry/Entity Type

Electronics

Contact Information for Business Card

Mark T. Doverly
President
Phone: 555.418.2096 Cell: 256.7193058 mtdoverly@brightlinkradio.biz
Brightlink Radio Systems
Harlow Springs, TN. 35871

```html
<!DOCTYPE html>
<html lang="en">
<head>
<meta charset="utf-8">
<title>Brightlink Radio Systems – Business Card</title>
<link rel="stylesheet" href="https://fonts.googleapis.com/css2?family=Gelasio:wght@700&display=swap">
<style>
  :root {
    --backdrop: #e9e3d8;
    --card: #ffffff;
    --brand-teal: #6cc5cc;
    --ink-dark: #1d2a3c;
    --name-blue: #3a6db3;
    --accent-orange: #f7901e;
    --detail-navy: #2b3a8f;
  }
  * { margin: 0; padding: 0; box-sizing: border-box; }
  html, body {
    width: 1200px;
    height: 960px;
    overflow: hidden;
    background: var(--backdrop);
    font-family: "Gelasio", Georgia, serif;
    font-weight: 700;
  }
  .business-card {
    position: absolute;
    left: 121px;
    top: 200px;
    width: 958px;
    height: 560px;
    background: var(--card);
    border-radius: 17px;
  }
  .brand-name {
    position: absolute;
    left: 59px;
    top: 36px;
    font-size: 41px;
    line-height: 48px;
    color: var(--brand-teal);
  }
  .service-line {
    position: absolute;
    left: 63px;
    top: 140px;
    font-size: 19px;
    line-height: 24px;
    color: var(--ink-dark);
  }
  .divider {
    position: absolute;
    left: 48px;
    width: 866px;
    height: 4px;
    background: var(--accent-orange);
  }
  .divider--top { top: 183px; }
  .divider--bottom { top: 406px; }
  .person {
    position: absolute;
    left: 0;
    width: 100%;
    text-align: center;
  }
  .person-name {
    top: 232px;
    font-size: 62px;
    line-height: 74px;
    color: var(--name-blue);
    padding-left: 6px;
  }
  .person-title {
    top: 304px;
    font-size: 31px;
    line-height: 36px;
    color: var(--name-blue);
  }
  .contact {
    position: absolute;
    font-size: 21px;
    line-height: 27px;
    white-space: nowrap;
  }
  .contact-label { color: var(--accent-orange); text-align: right; }
  .contact-value { color: var(--detail-navy); }
  .label-left { right: 810px; }
  .value-left { left: 173px; }
  .label-right { right: 261px; }
  .value-right { left: 720px; }
  .row-1 { top: 424px; }
  .row-2 { top: 458px; }
  .row-2-right { top: 456px; }
  .row-3 { top: 485px; }
</style>
</head>
<body>
  <main class="business-card">
    <div class="brand-name">Brightlink<br>Radio Systems</div>
    <p class="service-line">OrbiqView | Plate Linkway | Valtor Internet | Wi Fi systems</p>

    <div class="divider divider--top"></div>

    <h1 class="person person-name">Mark T. Doverly</h1>
    <p class="person person-title">President</p>

    <div class="divider divider--bottom"></div>

    <span class="contact contact-label label-left row-1">Email:</span>
    <span class="contact contact-value value-left row-1">mtdoverly@brightlinkradio.biz</span>
    <span class="contact contact-label label-left row-2">Address:</span>
    <span class="contact contact-value value-left row-2">Brightlink Radio Systems</span>
    <span class="contact contact-value value-left row-3">Harlow Springs, TN. 35871</span>

    <span class="contact contact-label label-right row-1">Cell:</span>
    <span class="contact contact-value value-right row-1">555.719.3058</span>
    <span class="contact contact-label label-right row-2-right">Phone:</span>
    <span class="contact contact-value value-right row-2-right">555.418.2096</span>
  </main>
</body>
</html>
```